vQ CARELINE (Brochure Design)

i need a proffesional brochure made. we are a mobile medical service company providing mobile Arterial Blood Gases(ABG's). Respiratory & Ventilator Consultation services. Ventilator and Tracheostomy training courses. and mobile vaccine administration.

this is my first time making a brochure so any and all advice/guidance will be appreciated.

i am thinking prints will be 8.5 inches x 11 inches (TRI-FOLD and BI-FOLD)

i have uploaded my business card design and logo design for reference.
as this brochure project continues ill update needs of the project descriptions.

Introduction: At vq CARELINE, we're dedicated to enhancing healthcare services by providing exceptional mobile arterial blood gases, respiratory and ventilator consultation services. Our core values revolve around excellence, compassion and accessibility. We believe that every individual deserves the highest standard of care, and we're committed to delivering that through expert guidance and top-notch training courses. Your health is at the heart of what we do, and we're here to support you on your journey to better respiratory health.

Mobile Arterial Blood Gases : Our mobile Arterial Blood Gas service offers quick, on-the-spot analysis of pH, oxygen, and carbon dioxide levels in your the blood. This service enables rapid adjustments to treatment plans for more effective respiratory care.

Ventilator and Tracheostomy Training: Our ventilator and tracheostomy course empowers caregivers and healthcare professionals to manage ventilators and care for tracheostomy patients with expertise. This training enhances patient safety, treatment outcomes, and healthcare provider confidence. vQ Careline your choice for top-notch care, convenience, and peace of mind.

Respiratory Consulting: Our respiratory consulting services provide expert guidance and support for individuals with respiratory / ventilator concerns. Benefits include personalized treatment plans, better management of respiratory conditions, and improved overall lung health. vQ Careline is your trusted partner for a breath of fresh air.

Target Market(s)

Sub-Acute facilities, Pulmonary Clinics, Pulmonologists, Nurses, Caregivers, Hospice and homehealth companies.

Industry/Entity Type

Medical; Respiratory; Nursing

Requirements
Must have
• proffesional simple design.

```html
<!DOCTYPE html>
<html lang="en">
<head>
<meta charset="utf-8">
<title>vQ CARELINE – Tri-fold Brochure</title>
<link rel="stylesheet" href="https://fonts.googleapis.com/css2?family=Open+Sans:wght@400;600;700;800&display=swap">
<style>
:root{
  --blue:#1d63b0;
  --navy:#153f78;
  --green:#5bb432;
  --green-dark:#3f8f22;
  --sky:#e6f0fa;
  --ink:#2b3440;
  --muted:#5d6875;
  --paper:#ffffff;
  --stage:#dfe3e8;
  --photo-warm:#c9b8a8;
  --photo-cool:#9fb6cc;
  --device:#cfd6dd;
}
*{box-sizing:border-box;margin:0;padding:0}
html,body{width:804px;height:1200px;overflow:hidden}
body{background:var(--stage);font-family:"Open Sans",Arial,sans-serif;color:var(--ink);position:relative}
.spread{position:absolute;left:22px;width:760px;height:587px;background:var(--paper);display:flex;box-shadow:0 2px 6px rgba(0,0,0,.18)}
.spread--outside{top:8px}
.spread--inside{top:605px}
.panel{position:relative;width:253.33px;height:100%;overflow:hidden}
.panel + .panel{border-left:1px solid rgba(0,0,0,.06)}
.photo{position:absolute;left:0;right:0}
.photo--warm{background:linear-gradient(135deg,#d8c7b6,#a99584 60%,#7f8ea0)}
.photo--cool{background:linear-gradient(160deg,#c3d4e6,#8aa6c3 55%,#5f7ea3)}
.photo--device{background:linear-gradient(180deg,#eef1f4,var(--device));border:1px solid #b8c1ca;border-radius:4px}
.wave{position:absolute;left:0;width:100%}
.heading{font-weight:800;font-size:15px;letter-spacing:.2px}
.heading--white{color:#fff}
.heading--blue{color:var(--blue)}
.body-text{font-size:7.6px;line-height:1.5;color:var(--muted)}
.body-text--white{color:#e8f0fa}
.brand{display:flex;align-items:center;gap:6px;font-weight:800;font-size:15px;color:#fff;letter-spacing:.5px}
.brand-mark{width:14px;height:14px;background:#fff;border-radius:50%;flex:none}
.band-title{position:absolute;left:0;right:0;height:30px;padding:6px 16px}
.contact-list{list-style:none;font-size:8.5px;color:var(--ink)}
.contact-list li{display:flex;align-items:center;gap:7px;margin-bottom:6px}
.contact-icon{width:16px;height:16px;border-radius:50%;background:var(--green);flex:none;display:flex;align-items:center;justify-content:center}
.card{position:absolute;background:#fff;border-radius:4px;padding:10px 12px}
.range-table{width:100%;border-collapse:collapse;font-size:7.5px;margin-top:8px}
.range-table th{background:var(--blue);color:#fff;padding:3px;text-align:left;font-weight:700}
.range-table td{padding:3px;border-bottom:1px solid #d5dee8;color:var(--ink)}
.service-list{list-style:none}
.service-list li{display:flex;gap:9px;margin-bottom:12px;align-items:flex-start}
.service-dot{width:26px;height:26px;border-radius:50%;background:var(--blue);flex:none;display:flex;align-items:center;justify-content:center}
.service-list h4{font-size:8.5px;color:var(--navy);margin-bottom:2px}
.web-bar{position:absolute;left:0;right:0;bottom:0;height:26px;background:var(--navy);color:#fff;font-size:9px;font-weight:700;text-align:center;line-height:26px;letter-spacing:.5px}
.tagline{font-weight:800;font-size:12px;line-height:1.3;color:var(--navy)}
</style>
</head>
<body>

<!-- Outside spread -->
<section class="spread spread--outside">
  <!-- Inner flap -->
  <div class="panel" style="background:var(--blue)">
    <div class="photo photo--warm" style="top:0;height:250px" role="img" aria-label="Photo of a clinician drawing an arterial blood sample from a patient's arm"></div>
    <svg class="wave" style="top:220px" width="254" height="50" viewBox="0 0 254 50" preserveAspectRatio="none">
      <path d="M0 30 C80 0 170 55 254 15 L254 50 L0 50Z" fill="var(--green)"/>
      <path d="M0 40 C90 12 170 60 254 28 L254 50 L0 50Z" fill="var(--blue)"/>
    </svg>
    <div style="position:absolute;top:272px;left:18px;right:18px">
      <h2 class="heading heading--white">Lorem Ipsum</h2>
      <p class="body-text body-text--white" style="margin-top:8px">At vQ CARELINE, we're dedicated to enhancing healthcare services by providing exceptional mobile arterial blood gases, respiratory and ventilator consultation services. Our core values revolve around excellence, compassion and accessibility.</p>
      <p class="body-text body-text--white" style="margin-top:8px">We believe every individual deserves the highest standard of care, delivered through expert guidance and top-notch training courses. Your health is at the heart of what we do.</p>
    </div>
    <div class="card" style="left:18px;right:18px;bottom:22px;height:70px">
      <h3 class="heading heading--blue" style="font-size:11px">Who We Serve</h3>
      <p class="body-text" style="margin-top:4px">Sub-acute facilities, pulmonary clinics, pulmonologists, nurses, caregivers, hospice and home health companies.</p>
    </div>
  </div>

  <!-- Back panel -->
  <div class="panel">
    <div class="band-title" style="top:0;height:62px;background:var(--green);padding:14px 18px">
      <div class="brand"><span class="brand-mark"></span>vQ CARELINE</div>
    </div>
    <svg class="wave" style="top:54px" width="254" height="24" viewBox="0 0 254 24" preserveAspectRatio="none">
      <path d="M0 8 C90 24 170 0 254 10 L254 0 L0 0Z" fill="var(--green)"/>
    </svg>
    <div style="position:absolute;top:90px;left:20px;right:20px">
      <h2 style="font-size:16px;font-weight:800;color:var(--navy)">Daniel Reyes</h2>
      <p style="font-size:9px;color:var(--green-dark);font-weight:700;margin-bottom:12px">Director</p>
      <ul class="contact-list">
        <li><span class="contact-icon"><svg width="9" height="9" viewBox="0 0 24 24"><path d="M6.6 10.8a15 15 0 0 0 6.6 6.6l2.2-2.2a1 1 0 0 1 1-.25 11 11 0 0 0 3.6.6 1 1 0 0 1 1 1V20a1 1 0 0 1-1 1A17 17 0 0 1 3 4a1 1 0 0 1 1-1h3.5a1 1 0 0 1 1 1c0 1.25.2 2.45.6 3.6a1 1 0 0 1-.25 1z" fill="#fff"/></svg></span>555-014-2290</li>
        <li><span class="contact-icon"><svg width="9" height="9" viewBox="0 0 24 24"><path d="M6.6 10.8a15 15 0 0 0 6.6 6.6l2.2-2.2a1 1 0 0 1 1-.25 11 11 0 0 0 3.6.6 1 1 0 0 1 1 1V20a1 1 0 0 1-1 1A17 17 0 0 1 3 4a1 1 0 0 1 1-1h3.5a1 1 0 0 1 1 1c0 1.25.2 2.45.6 3.6a1 1 0 0 1-.25 1z" fill="#fff"/></svg></span>555-014-2291</li>
        <li><span class="contact-icon"><svg width="9" height="9" viewBox="0 0 24 24"><path d="M3 5h18v14H3z M3 5l9 7 9-7" fill="none" stroke="#fff" stroke-width="2.5"/></svg></span>hello@vqcareline.com</li>
        <li><span class="contact-icon"><svg width="9" height="9" viewBox="0 0 24 24"><path d="M12 2a7 7 0 0 0-7 7c0 5 7 13 7 13s7-8 7-13a7 7 0 0 0-7-7zm0 9.5A2.5 2.5 0 1 1 12 6.5a2.5 2.5 0 0 1 0 5z" fill="#fff"/></svg></span>www.vqcareline.com</li>
      </ul>
    </div>
    <div class="photo photo--device" style="top:262px;left:24px;right:24px;height:150px" role="img" aria-label="Photo of a portable blood gas analyzer"></div>
    <div style="position:absolute;top:430px;left:20px;right:20px">
      <p class="tagline" style="font-size:11px">Mobile Medical Service company providing Mobile Arterial Blood Gases (ABG's)</p>
      <p class="body-text" style="margin-top:6px">Respiratory &amp; ventilator consultation, ventilator and tracheostomy training, and mobile vaccine administration.</p>
    </div>
    <div class="web-bar" style="background:var(--blue)">www.vqcareline.com</div>
  </div>

  <!-- Cover -->
  <div class="panel">
    <div class="band-title" style="top:0;height:58px;background:var(--blue);padding:16px 18px">
      <div class="brand" style="justify-content:flex-end"><span class="brand-mark"></span>vQ CARELINE</div>
    </div>
    <div class="photo photo--cool" style="top:58px;height:200px" role="img" aria-label="Photo of a patient resting on a ventilator in a hospital bed"></div>
    <svg class="wave" style="top:220px" width="254" height="60" viewBox="0 0 254 60" preserveAspectRatio="none">
      <path d="M0 20 C80 55 170 0 254 30 L254 60 L0 60Z" fill="var(--blue)"/>
      <path d="M0 30 C90 60 170 12 254 40 L254 60 L0 60Z" fill="var(--green)"/>
      <path d="M0 42 C90 66 170 28 254 52 L254 60 L0 60Z" fill="#fff"/>
    </svg>
    <div class="photo photo--device" style="top:290px;left:26px;width:110px;height:100px" role="img" aria-label="Photo of blood gas monitoring equipment"></div>
    <div class="photo photo--device" style="top:300px;left:146px;width:82px;height:90px" role="img" aria-label="Photo of a ventilator display"></div>
    <div style="position:absolute;top:408px;left:20px;right:20px">
      <p class="tagline">Mobile Medical Service company providing Mobile Arterial Blood Gases (ABG's)</p>
      <p class="body-text" style="margin-top:8px;color:var(--ink)"><strong>Respiratory &amp; Ventilator Consultation</strong><br>Ventilator &amp; Tracheostomy Training<br>Mobile Vaccine Administration</p>
    </div>
    <div class="web-bar">www.vqcareline.com</div>
  </div>
</section>

<!-- Inside spread -->
<section class="spread spread--inside">
  <!-- Panel 1 -->
  <div class="panel" style="background:var(--sky)">
    <div class="band-title" style="top:18px;background:var(--blue);width:70%">
      <h2 class="heading heading--white">Lorem Ipsum</h2>
    </div>
    <div class="card" style="top:60px;left:16px;right:16px">
      <p class="body-text">Our mobile Arterial Blood Gas service offers quick, on-the-spot analysis of pH, oxygen, and carbon dioxide levels in the blood. This enables rapid adjustments to treatment plans for more effective respiratory care.</p>
      <table class="range-table">
        <thead><tr><th>Value</th><th>Normal Range</th></tr></thead>
        <tbody>
          <tr><td>pH</td><td>7.35 – 7.45</td></tr>
          <tr><td>PaO₂</td><td>75 – 100 mmHg</td></tr>
          <tr><td>PaCO₂</td><td>35 – 45 mmHg</td></tr>
          <tr><td>HCO₃</td><td>22 – 26 mEq/L</td></tr>
          <tr><td>SaO₂</td><td>94 – 100 %</td></tr>
        </tbody>
      </table>
    </div>
    <div class="photo photo--warm" style="top:360px;left:16px;right:16px;height:190px;border-radius:4px" role="img" aria-label="Photo of a gloved hand taking a blood sample from a patient's arm"></div>
  </div>

  <!-- Panel 2 -->
  <div class="panel">
    <div style="position:absolute;top:20px;left:18px;right:18px">
      <p class="body-text">Our ventilator and tracheostomy course empowers caregivers and healthcare professionals to manage ventilators and care for tracheostomy patients with expertise. This training enhances patient safety, treatment outcomes, and provider confidence.</p>
    </div>
    <div class="photo photo--device" style="top:100px;left:18px;right:18px;height:200px" role="img" aria-label="Photo of a ventilator unit on a stand"></div>
    <svg class="wave" style="top:318px" width="254" height="269" viewBox="0 0 254 269" preserveAspectRatio="none">
      <path d="M0 20 C90 0 170 40 254 10 L254 269 L0 269Z" fill="var(--blue)"/>
      <path d="M0 20 C90 0 170 40 254 10 L254 18 C170 48 90 8 0 28Z" fill="var(--green)"/>
    </svg>
    <div style="position:absolute;top:362px;left:18px;right:18px">
      <h2 class="heading heading--white">Lorem Ipsum</h2>
      <p class="body-text body-text--white" style="margin-top:8px">Our respiratory consulting services provide expert guidance and support for individuals with respiratory and ventilator concerns. Benefits include personalized treatment plans, better management of respiratory conditions, and improved overall lung health.</p>
      <p class="body-text body-text--white" style="margin-top:8px">vQ Careline is your trusted partner for a breath of fresh air.</p>
    </div>
  </div>

  <!-- Panel 3 -->
  <div class="panel">
    <div class="band-title" style="top:18px;left:auto;width:75%;background:var(--green);text-align:right">
      <h2 class="heading heading--white">Lorem Ipsum</h2>
    </div>
    <ul class="service-list" style="position:absolute;top:66px;left:18px;right:18px">
      <li><span class="service-dot"><svg width="12" height="12" viewBox="0 0 24 24"><path d="M4 12l5 5L20 6" fill="none" stroke="#fff" stroke-width="3"/></svg></span><div><h4>Mobile ABG Testing</h4><p class="body-text">On-site blood gas analysis with fast results.</p></div></li>
      <li><span class="service-dot"><svg width="12" height="12" viewBox="0 0 24 24"><path d="M4 12l5 5L20 6" fill="none" stroke="#fff" stroke-width="3"/></svg></span><div><h4>Respiratory Consulting</h4><p class="body-text">Personalized plans for ventilator patients.</p></div></li>
      <li><span class="service-dot"><svg width="12" height="12" viewBox="0 0 24 24"><path d="M4 12l5 5L20 6" fill="none" stroke="#fff" stroke-width="3"/></svg></span><div><h4>Trach &amp; Vent Training</h4><p class="body-text">Hands-on courses for staff and caregivers.</p></div></li>
      <li><span class="service-dot"><svg width="12" height="12" viewBox="0 0 24 24"><path d="M4 12l5 5L20 6" fill="none" stroke="#fff" stroke-width="3"/></svg></span><div><h4>Mobile Vaccines</h4><p class="body-text">Vaccine administration at your facility.</p></div></li>
    </ul>
    <div class="card" style="left:18px;right:18px;bottom:20px;background:var(--sky)">
      <h3 class="heading heading--blue" style="font-size:11px">Why Choose Us</h3>
      <p class="body-text" style="margin-top:4px">vQ Careline is your choice for top-notch care, convenience, and peace of mind, wherever your patients are.</p>
    </div>
  </div>
</section>

</body>
</html>
```